Beautiful Upgraded Single Story Home in Brindlemere...SOLD in 3 days for top $$!

This is a 6.5" x 11" EDDM postcard. Please use the indicia files and 6.5" x 11" template attached in the brief.
Updates

Project Deadline Extended
Reason: We are still working on the details for one of the postcards. Thanks

Target Market(s)

Listings

Font styles to use
Serif

Colors
33b8a4

Requirements
Must have
• Call me if you are interested in getting the most amount of equity out of your home!
• Marisol Pendry (555) 417-2963 and Tamsin Okavell (555) 730-4186
• Marisol@TeamOkavell.example and Tamsin@TeamOkavell.example
• Harbor Ridge Homes
• The Key to your Real Estate Needs!
• (At bottom of postcard) "If you are currently listed with a licensed Realtor, this is not intended as solicitation"
Nice to have
• The Front Should be the Property Picture and "In Escrow in 3 Days!"

```html
<!DOCTYPE html>
<html lang="en">
<head>
<meta charset="utf-8">
<title>In Escrow in 3 Days! – Harbor Ridge Homes Postcard</title>
<link href="https://fonts.googleapis.com/css2?family=Merriweather:wght@400&family=Mulish:ital,wght@0,400;0,500;0,600;1,400&display=swap" rel="stylesheet">
<style>
  :root {
    --teal: #33b8a4;
    --teal-deep: #24a08d;
    --ink: #1f1f1f;
    --paper: #ffffff;
    --backdrop: #e9ebea;
    --sky: #c9dbe8;
    --lawn: #7d9a4a;
    --stucco: #b9a58a;
    --portrait-a: #3d5f63;
    --portrait-b: #c9b79c;
  }
  * { box-sizing: border-box; margin: 0; padding: 0; }
  html, body { width: 1200px; height: 900px; overflow: hidden; }
  body {
    background: var(--backdrop);
    font-family: "Mulish", sans-serif;
    color: var(--ink);
    display: flex;
    flex-direction: column;
    align-items: center;
    justify-content: center;
    gap: 36px;
  }
  .postcard {
    position: relative;
    width: 680px;
    height: 402px;
    background: var(--paper);
    overflow: hidden;
    box-shadow: 0 6px 18px rgba(0,0,0,.18);
  }

  /* Front */
  .property-photo {
    position: absolute; inset: 0;
    background:
      linear-gradient(180deg, var(--sky) 0%, var(--sky) 30%, var(--stucco) 48%, #a99a82 62%, var(--lawn) 76%, #5f7d37 100%);
  }
  .headline-band {
    position: absolute; left: 0; right: 0; top: 92px; height: 78px;
    background: var(--teal);
    display: flex; align-items: center; justify-content: center;
  }
  .headline {
    font-family: "Merriweather", serif;
    font-weight: 400;
    font-size: 38px;
    color: var(--paper);
    letter-spacing: .5px;
  }
  .indicia {
    position: absolute; top: 14px; right: 16px;
    width: 58px; height: 46px;
    background: var(--paper);
    border: 1px solid var(--ink);
    font-size: 6px; line-height: 1.2; text-align: center;
    padding: 5px 2px; text-transform: uppercase;
  }
  .mailing-panel {
    position: absolute; right: 16px; bottom: 20px;
    width: 190px; height: 68px;
    background: var(--paper);
    padding: 12px 12px;
    font-size: 11px; line-height: 1.25;
  }
  .mailing-panel .route { font-size: 6px; letter-spacing: 1px; margin-bottom: 8px; }

  /* Back */
  .agents-photo {
    position: absolute; left: 0; top: 0; width: 300px; height: 326px;
    background: linear-gradient(135deg, var(--portrait-a) 0%, #6e8f8b 45%, var(--portrait-b) 100%);
  }
  .contact-panel {
    position: absolute; left: 300px; top: 0; right: 0; height: 326px;
    background: var(--paper);
    padding: 30px 34px 0 40px;
  }
  .brand {
    display: flex; align-items: center; justify-content: center; gap: 10px;
    margin: 0 auto 32px;
    font-family: "Mulish", sans-serif;
    font-weight: 500;
    font-size: 22px;
    color: var(--ink);
  }
  .brand-mark { width: 14px; height: 14px; background: var(--ink); }
  .contact-list { list-style: none; font-size: 15px; line-height: 1.28; }
  .contact-list .name { color: var(--teal); }
  .contact-group { margin-bottom: 14px; }
  .tagline { color: var(--teal); }
  .disclaimer-band {
    position: absolute; left: 0; right: 0; bottom: 0; height: 76px;
    background: var(--teal);
    display: flex; flex-direction: column; align-items: center; justify-content: center;
    gap: 8px;
    padding: 0 20px;
    text-align: center;
  }
  .call-to-action {
    font-weight: 600; font-size: 14px; color: var(--paper); letter-spacing: .2px;
  }
  .disclaimer {
    font-style: italic; font-size: 13px; color: var(--paper); letter-spacing: .2px;
  }
</style>
</head>
<body>

  <section class="postcard postcard-front" aria-label="Postcard front">
    <div class="property-photo" role="img" aria-label="Photo of a single story stucco home with a two-car garage, green lawn and trees under a blue sky"></div>
    <div class="headline-band"><h1 class="headline">In Escrow in 3 Days!</h1></div>
    <div class="indicia">Prsrt Std Ecrwss U.S. Postage Paid Eddm Retail</div>
    <div class="mailing-panel">
      <p class="route">ECRWSS EDDM</p>
      <p>Local<br>Postal Customer</p>
    </div>
  </section>

  <section class="postcard postcard-back" aria-label="Postcard back">
    <div class="agents-photo" role="img" aria-label="Portrait photo of the two agents standing together in front of a colorful storefront"></div>
    <div class="contact-panel">
      <div class="brand"><span class="brand-mark"></span>Harbor Ridge Homes</div>
      <ul class="contact-list">
        <li class="contact-group">
          <span class="name">Marisol Pendry</span> (555) 417-2963<br>
          <span class="name">Tamsin Okavell</span> (555) 730-4186
        </li>
        <li class="contact-group">
          Marisol@<span class="name">TeamOkavell</span>.example<br>
          Tamsin@<span class="name">TeamOkavell</span>.example
        </li>
        <li class="contact-group">
          Harbor Ridge Homes<br>
          <span class="tagline">The Key to your Real Estate Needs!</span>
        </li>
      </ul>
    </div>
    <div class="disclaimer-band">
      <p class="call-to-action">Call me if you are interested in getting the most amount of equity out of your home!</p>
      <p class="disclaimer">"If you are currently listed with a licensed Realtor, this is not intended as solicitation"</p>
    </div>
  </section>

</body>
</html>
```